Diagram for consulting firm website

My consulting firm, Tamsworth Consulting, www.tamsworthconsulting-example.com.au, requires a visual diagram in the style and colours of our website to promote "Restructuring services." Please see the two attached files for content and guidance.

```html
<!DOCTYPE html>
<html lang="en">
<head>
<meta charset="utf-8">
<title>Restructuring Services – Tamsworth Consulting</title>
<link rel="stylesheet" href="https://fonts.googleapis.com/css2?family=Montserrat:wght@500;600;700&display=swap">
<style>
  :root {
    --navy: #0d3580;
    --orange: #f7931e;
    --cyan: #00aeef;
    --white: #ffffff;
  }
  html, body {
    margin: 0;
    padding: 0;
    width: 960px;
    height: 1200px;
    overflow: hidden;
    background: var(--white);
  }
  .diagram {
    display: block;
    width: 960px;
    height: 1200px;
    font-family: "Montserrat", Arial, sans-serif;
  }
  .hub-title { fill: var(--white); font-size: 34px; font-weight: 700; text-anchor: middle; }
  .step-number { fill: var(--white); font-size: 32px; font-weight: 700; text-anchor: middle; dominant-baseline: central; }
  .pill-label { fill: var(--navy); font-size: 20px; font-weight: 600; text-anchor: middle; dominant-baseline: central; }
  .connector { stroke: var(--navy); stroke-width: 4; fill: none; }
  .brand-name { fill: var(--navy); font-size: 34px; font-weight: 700; }
  .cashflow-label { fill: var(--navy); font-size: 28px; font-weight: 600; text-anchor: middle; }
  .path-label { fill: var(--navy); font-size: 16px; font-weight: 600; text-anchor: middle; }
  .bullet-list { fill: var(--navy); font-size: 12px; font-weight: 500; }
  .stage-label { fill: var(--navy); font-size: 16px; font-weight: 700; }
  .stage-label.center { text-anchor: middle; }
  .arc-label { fill: var(--navy); font-size: 30px; font-weight: 700; }
  .scale-label { fill: var(--navy); font-size: 17px; font-weight: 600; text-anchor: middle; }
  .direction-line { stroke: var(--navy); stroke-width: 3; fill: none; }
</style>
</head>
<body>
<svg class="diagram" viewBox="0 0 1200 1500" xmlns="http://www.w3.org/2000/svg" role="img" aria-label="Types of corporate restructuring and the restructuring journey from cash flow good to cash flow poor">
  <defs>
    <linearGradient id="pill-stroke" x1="0" x2="1" y1="0" y2="0">
      <stop offset="0.5" stop-color="#f7931e"/>
      <stop offset="0.5" stop-color="#00aeef"/>
    </linearGradient>
    <marker id="arrowhead" viewBox="0 0 10 10" refX="8" refY="5" markerWidth="6" markerHeight="6" orient="auto">
      <path d="M0 0 L10 5 L0 10 Z" fill="#0d3580"/>
    </marker>
    <pattern id="ticks-success" patternUnits="userSpaceOnUse" x="190" y="0" width="25.6" height="40">
      <rect x="0" y="0" width="2" height="40" fill="#f7931e"/>
    </pattern>
    <pattern id="ticks-stressed" patternUnits="userSpaceOnUse" x="395" y="0" width="12.8" height="40">
      <rect x="0" y="0" width="2" height="40" fill="#f7931e"/>
    </pattern>
    <pattern id="ticks-distressed" patternUnits="userSpaceOnUse" x="600" y="0" width="8.5" height="40">
      <rect x="0" y="0" width="2" height="40" fill="#f7931e"/>
    </pattern>
    <pattern id="ticks-insolvent" patternUnits="userSpaceOnUse" x="805" y="0" width="5.7" height="40">
      <rect x="0" y="0" width="2" height="40" fill="#f7931e"/>
    </pattern>
    <path id="control-arc" d="M195 860 A405 405 0 0 0 1005 860"/>
  </defs>

  <!-- Types of restructuring -->
  <g class="restructuring-types">
    <path class="connector" d="M320 118 A180 180 0 0 1 320 478"/>
    <line class="connector" x1="320" y1="118" x2="515" y2="118"/>
    <line class="connector" x1="485" y1="228" x2="682" y2="228"/>
    <line class="connector" x1="485" y1="368" x2="682" y2="368"/>
    <line class="connector" x1="320" y1="478" x2="515" y2="478"/>

    <circle cx="320" cy="298" r="140" fill="var(--navy)"/>
    <text class="hub-title" x="320" y="267">Types of</text>
    <text class="hub-title" x="320" y="307">Corporate</text>
    <text class="hub-title" x="320" y="347">Restructuring</text>

    <g class="step">
      <circle cx="320" cy="118" r="30" fill="var(--cyan)"/>
      <text class="step-number" x="320" y="119">1</text>
      <rect x="513" y="92" width="342" height="52" rx="26" fill="var(--white)" stroke="url(#pill-stroke)" stroke-width="4"/>
      <text class="pill-label" x="684" y="118">Financial Restructuring</text>
    </g>
    <g class="step">
      <circle cx="485" cy="228" r="30" fill="var(--cyan)"/>
      <text class="step-number" x="485" y="229">2</text>
      <rect x="680" y="202" width="340" height="52" rx="26" fill="var(--white)" stroke="url(#pill-stroke)" stroke-width="4"/>
      <text class="pill-label" x="850" y="228">Operational Restructuring</text>
    </g>
    <g class="step">
      <circle cx="485" cy="368" r="30" fill="var(--cyan)"/>
      <text class="step-number" x="485" y="369">3</text>
      <rect x="680" y="342" width="340" height="52" rx="26" fill="var(--white)" stroke="url(#pill-stroke)" stroke-width="4"/>
      <text class="pill-label" x="850" y="368">Organizational Restructuring</text>
    </g>
    <g class="step">
      <circle cx="320" cy="478" r="30" fill="var(--cyan)"/>
      <text class="step-number" x="320" y="479">4</text>
      <rect x="513" y="452" width="342" height="52" rx="26" fill="var(--white)" stroke="url(#pill-stroke)" stroke-width="4"/>
      <text class="pill-label" x="684" y="478">Strategic Restructuring</text>
    </g>
  </g>

  <!-- Brand divider -->
  <g class="brand-divider">
    <rect x="0" y="650" width="420" height="18" fill="var(--orange)"/>
    <rect x="770" y="650" width="430" height="18" fill="var(--cyan)"/>
    <circle cx="485" cy="658" r="32" fill="var(--orange)"/>
    <text class="brand-name" x="532" y="652">Tamsworth</text>
    <text class="brand-name" x="532" y="692">Consulting</text>
  </g>

  <!-- Restructuring journey -->
  <g class="journey">
    <text class="cashflow-label" x="310" y="780">Cash Flow Good</text>
    <text class="cashflow-label" x="897" y="780">Cash Flow Poor</text>

    <path d="M200 860 A400 400 0 0 0 1000 860" fill="none" stroke="var(--orange)" stroke-width="60"/>
    <polygon points="920,871 1080,871 1000,790" fill="var(--orange)"/>
    <text class="arc-label"><textPath href="#control-arc" startOffset="50%" text-anchor="middle">Loss of Management Control</textPath></text>

    <line class="direction-line" x1="600" y1="860" x2="268" y2="998" marker-end="url(#arrowhead)"/>
    <line class="direction-line" x1="600" y1="860" x2="463" y2="1190" marker-end="url(#arrowhead)"/>
    <line class="direction-line" x1="600" y1="860" x2="738" y2="1190" marker-end="url(#arrowhead)"/>
    <line class="direction-line" x1="600" y1="860" x2="930" y2="998" marker-end="url(#arrowhead)"/>
    <circle cx="600" cy="860" r="15" fill="var(--navy)"/>

    <text class="path-label" transform="translate(436 919) rotate(-22.6)">Underperforming Business</text>
    <text class="path-label" transform="translate(766 918) rotate(22.6)">Insolvent Business</text>

    <text class="bullet-list" x="310">
      <tspan x="310" y="1019">• Potensial Covenant Breach</tspan>
      <tspan x="310" y="1033">• Credit Rating Downgrade</tspan>
      <tspan x="310" y="1048">• Profit Warning</tspan>
      <tspan x="310" y="1062">• Board Still in Control of Strategy</tspan>
    </text>
    <text class="bullet-list" x="503">
      <tspan x="503" y="1119">• Covenant Breach(es)</tspan>
      <tspan x="503" y="1133">• Creditor Pressure</tspan>
      <tspan x="503" y="1148">• Expensive re-financing</tspan>
      <tspan x="503" y="1162">• Equity value negligible</tspan>
      <tspan x="503" y="1177">• Creditor in Control of Strategy</tspan>
    </text>

    <text class="stage-label" x="130">
      <tspan x="130" y="1133">Distressed</tspan>
      <tspan x="130" y="1153">Operational</tspan>
      <tspan x="130" y="1173">Restructuring</tspan>
    </text>
    <text class="stage-label" x="963">
      <tspan x="963" y="1133">Formal</tspan>
      <tspan x="963" y="1153">Insolvency</tspan>
      <tspan x="963" y="1173">Appointment</tspan>
    </text>
    <text class="stage-label center" x="600">
      <tspan x="600" y="1327">Creditor Advisory/Distressed</tspan>
      <tspan x="600" y="1347">Corporate Advisory (Financial)</tspan>
    </text>
  </g>

  <!-- Distress scale -->
  <g class="distress-scale">
    <text class="scale-label" x="292" y="1404">Success</text>
    <text class="scale-label" x="497" y="1404">Stressed</text>
    <text class="scale-label" x="702" y="1404">Distressed</text>
    <text class="scale-label" x="907" y="1404">Insolvent</text>

    <rect x="190" y="1414" width="205" height="30" fill="url(#ticks-success)"/>
    <rect x="395" y="1414" width="205" height="30" fill="url(#ticks-stressed)"/>
    <rect x="600" y="1414" width="205" height="30" fill="url(#ticks-distressed)"/>
    <rect x="805" y="1414" width="205" height="30" fill="url(#ticks-insolvent)"/>

    <rect x="187" y="1409" width="5" height="40" fill="var(--orange)"/>
    <rect x="393" y="1409" width="5" height="40" fill="var(--orange)"/>
    <rect x="598" y="1409" width="5" height="40" fill="var(--orange)"/>
    <rect x="803" y="1409" width="5" height="40" fill="var(--orange)"/>
    <rect x="1008" y="1409" width="5" height="40" fill="var(--orange)"/>
  </g>
</svg>
</body>
</html>
```